Design a helpdesk ticketing platform *

We are launching a helpdesk ticketing platform. Very much like lumidesk.example, brightowl.example, calmhub.example, tidyqueue.example etc. We have a full mid-fidelity prototype built and we want someone to build the full fidelity of the product.

You can view the full mid-fidelity prototype here: https://shortlink.example/Qw8pLk

The best way moving forward is to just design the following 4 pages

- Main Dashboard https://shortlink.example/48vRxN
- All tickets https://shortlink.example/jbdYsW
- Viewing a ticket https://shortlink.example/mHqLtB
- Contacts https://shortlink.example/yKeoPd

Target Market(s)

Small business owners

Industry/Entity Type

Saas

Number of Pages Required

4 page

Font styles to use
Serif
Sans Serif

Colors

Designer to choose colors to be used in the design.

Requirements
Must have
• Must follow the prototype exactly. We are not looking for any UX changes. We want the designe xactly as the prototype is. We are only looking for design ideas.
Should not have
• modern, clean. We'd love to see the primary color as yellow, purple, orange, green or blue. You choose which one you think looks best and go with that.

```html
<!DOCTYPE html>
<html lang="en">
<head>
<meta charset="utf-8">
<title>DeskHarbor – Dashboard</title>
<link href="https://fonts.googleapis.com/css2?family=Roboto:wght@400;500;700&display=swap" rel="stylesheet">
<style>
  :root{
    --brand-bar:#24408d;
    --sidebar:#1e336f;
    --nav-item:#224a86;
    --nav-icon:#1f4079;
    --nav-active:#2d9fdc;
    --nav-active-icon:#2a8fcd;
    --green:#1f9e6e;
    --page:#e8eaef;
    --ink:#3a3a3a;
    --navy:#1e3370;
    --purple:#5a2fb4;
    --yellow:#d9b72a;
    --teal:#1b9e78;
    --grey:#a7a7a7;
    --blue:#2ea0df;
    --panel-head:#f3f3f3;
    --line:#dcdde0;
    --footer:#1a1a1a;
  }
  *{box-sizing:border-box;margin:0;padding:0}
  html,body{width:1200px;height:998px;overflow:hidden}
  body{font-family:'Roboto',Arial,sans-serif;background:var(--page);position:relative;color:var(--ink)}

  .sidebar{position:absolute;left:0;top:0;width:215px;height:940px;background:var(--sidebar)}
  .brand{height:86px;background:var(--brand-bar);display:flex;align-items:center;padding-left:37px;gap:22px}
  .brand-name{color:#fff;font-weight:700;font-size:24px;letter-spacing:-0.3px}
  .new-ticket{position:absolute;left:39px;top:113px;width:121px;height:32px;background:var(--green);border-radius:2px;color:#fff;font-size:14px;display:flex;align-items:center;padding-left:18px}
  .new-ticket .dots{position:absolute;right:11px;top:8px}
  .nav{position:absolute;top:168px;left:0;width:215px;list-style:none}
  .nav li{height:50px;display:flex;align-items:center;background:var(--nav-item);border-bottom:1px solid #1c3a6d;color:#fff;font-size:15.5px;position:relative}
  .nav .icon{width:59px;height:100%;background:var(--nav-icon);display:flex;align-items:center;justify-content:center}
  .nav .label{padding-left:13px}
  .nav li.active{background:var(--nav-active)}
  .nav li.active .icon{background:var(--nav-active-icon)}
  .nav .caret{position:absolute;right:18px;top:22px}

  .topbar{position:absolute;left:215px;top:0;width:985px;height:86px;background:#fff;box-shadow:0 1px 3px rgba(0,0,0,.08)}
  .page-title{position:absolute;left:41px;top:27px;font-size:26px;font-weight:500;color:#3c3c3c}
  .search{position:absolute;left:661px;top:22px;width:196px;height:38px;border:1px solid #555;border-radius:19px;font-size:13px;color:#333;display:flex;align-items:center;padding-left:14px}
  .search svg{position:absolute;right:14px;top:12px}
  .avatar{position:absolute;left:872px;top:17px;width:50px;height:50px;border-radius:50%;background:var(--navy);color:#fff;font-size:20px;display:flex;align-items:center;justify-content:center}

  .greeting{position:absolute;left:256px;top:131px;font-size:29px;color:#3a3a3a}
  .stats{position:absolute;left:258px;top:189px;display:flex;gap:8px}
  .stat{width:134px;height:88px;border-radius:2px;color:#fff;text-align:center;padding-top:12px;box-shadow:0 1px 2px rgba(0,0,0,.15)}
  .stat .num{font-size:32px;line-height:1;letter-spacing:1px}
  .stat .lbl{font-size:14.5px;margin-top:6px}
  .stat.open{background:var(--purple)}
  .stat.due{background:var(--yellow)}
  .stat.unassigned{background:var(--teal)}
  .stat.neutral{background:var(--grey);color:#222}
  .stat.unresolved{background:var(--blue)}

  .activity{position:absolute;left:257px;top:308px;width:844px;height:538px;background:#fff;border:1px solid var(--line);border-radius:2px}
  .activity-head{height:47px;background:var(--panel-head);border-bottom:1px solid var(--line);display:flex;align-items:center;padding-left:20px;gap:9px;font-size:17px;color:#333}
  .day{position:absolute;left:24px}
  .day-title{display:flex;align-items:center;gap:6px;color:var(--navy);font-size:16px;margin-left:4px}
  .day-title .ring{width:17px;height:17px;border:1.3px solid #333;border-radius:50%}
  .entry{margin-left:52px;font-size:12.5px;color:#333}
  .entry .time{display:flex;align-items:center;gap:5px;margin-top:11px}
  .entry p{margin-top:4px}
  .entry + .entry{margin-top:21px}

  .footer{position:absolute;left:0;top:940px;width:1200px;height:58px;background:var(--footer);color:#fff;font-size:11px;display:flex;align-items:center;justify-content:center}
</style>
</head>
<body>

<aside class="sidebar">
  <div class="brand">
    <span class="brand-name">DeskHarbor</span>
    <svg width="20" height="16" viewBox="0 0 20 16"><rect y="0" width="20" height="2.6" fill="#fff"/><rect y="6.7" width="20" height="2.6" fill="#fff"/><rect y="13.4" width="20" height="2.6" fill="#fff"/></svg>
  </div>
  <div class="new-ticket">New Ticket
    <svg class="dots" width="4" height="16" viewBox="0 0 4 16"><circle cx="2" cy="2" r="1.6" fill="#fff"/><circle cx="2" cy="8" r="1.6" fill="#fff"/><circle cx="2" cy="14" r="1.6" fill="#fff"/></svg>
  </div>
  <ul class="nav">
    <li class="active"><span class="icon"><svg width="18" height="15" viewBox="0 0 18 15"><path d="M9 1a8 8 0 0 0-8 8c0 2 .7 3.8 1.9 5h12.2A8 8 0 0 0 9 1z" fill="#fff"/><path d="M9 10l3-5" stroke="var(--nav-active-icon)" stroke-width="1.6"/><circle cx="9" cy="10" r="1.5" fill="var(--nav-active-icon)"/></svg></span><span class="label">Dashboard</span></li>
    <li><span class="icon"><svg width="19" height="13" viewBox="0 0 19 13"><rect x="0.5" y="0.5" width="18" height="12" rx="1.5" fill="#fff"/><rect x="4" y="3.5" width="11" height="6" fill="var(--nav-icon)"/></svg></span><span class="label">Ticket</span>
      <svg class="caret" width="12" height="7" viewBox="0 0 12 7"><path d="M0 0h12L6 7z" fill="#fff"/></svg></li>
    <li><span class="icon"><svg width="18" height="16" viewBox="0 0 18 16"><path d="M12 2H2v12h11V9" fill="none" stroke="#fff" stroke-width="1.8"/><path d="M8 10l1-3 7-6 2 2-7 6z" fill="#fff"/></svg></span><span class="label">Contacts</span></li>
    <li><span class="icon"><svg width="17" height="17" viewBox="0 0 17 17"><g fill="#fff"><circle cx="8.5" cy="8.5" r="5.5"/><rect x="7" y="0" width="3" height="17"/><rect x="0" y="7" width="17" height="3"/><rect x="7" y="0" width="3" height="17" transform="rotate(45 8.5 8.5)"/><rect x="7" y="0" width="3" height="17" transform="rotate(-45 8.5 8.5)"/></g><circle cx="8.5" cy="8.5" r="2.3" fill="var(--nav-icon)"/></svg></span><span class="label">Admin Setting</span>
      <svg class="caret" width="12" height="7" viewBox="0 0 12 7"><path d="M0 0h12L6 7z" fill="#fff"/></svg></li>
    <li><span class="icon"><svg width="14" height="17" viewBox="0 0 14 17"><path d="M0 0h9l5 5v12H0z" fill="#fff"/><path d="M3 8h8M3 11h8M3 14h8" stroke="var(--nav-icon)" stroke-width="1.3"/></svg></span><span class="label">Account &amp; Billing</span></li>
  </ul>
</aside>

<header class="topbar">
  <h1 class="page-title">Dashboard</h1>
  <div class="search">Search
    <svg width="14" height="14" viewBox="0 0 14 14"><circle cx="5.5" cy="5.5" r="4.3" fill="none" stroke="#111" stroke-width="2"/><path d="M8.7 8.7L13 13" stroke="#111" stroke-width="2.4" stroke-linecap="round"/></svg>
  </div>
  <div class="avatar">AK</div>
</header>

<main>
  <h2 class="greeting">Good Morning, Andrew</h2>
  <section class="stats">
    <div class="stat open"><div class="num">16</div><div class="lbl">Open Tickets</div></div>
    <div class="stat due"><div class="num">14</div><div class="lbl">Due Today</div></div>
    <div class="stat unassigned"><div class="num">14</div><div class="lbl">Unassigned</div></div>
    <div class="stat neutral"><div class="num">0</div><div class="lbl">Over Due</div></div>
    <div class="stat neutral"><div class="num">0</div><div class="lbl">On Hold</div></div>
    <div class="stat unresolved"><div class="num">11</div><div class="lbl">Not Resolved</div></div>
  </section>

  <section class="activity">
    <div class="activity-head">
      <svg width="18" height="14" viewBox="0 0 18 14"><g fill="#333"><rect x="0" y="0.5" width="3" height="3"/><rect x="0" y="5.5" width="3" height="3"/><rect x="0" y="10.5" width="3" height="3"/><rect x="5" y="1" width="13" height="2"/><rect x="5" y="6" width="13" height="2"/><rect x="5" y="11" width="13" height="2"/></g></svg>
      Recent Activities
    </div>

    <div class="day" style="top:70px">
      <div class="day-title"><span class="ring"></span>Today</div>
      <div class="entry"><div class="time"><svg width="6" height="9" viewBox="0 0 6 9"><path d="M1 1l3.5 3.5L1 8" fill="none" stroke="#222" stroke-width="1.8"/></svg>4.49 pm</div><p>Lorem Ipsum is simply dummy text of the printing and typesetting industry</p></div>
      <div class="entry"><div class="time"><svg width="6" height="9" viewBox="0 0 6 9"><path d="M1 1l3.5 3.5L1 8" fill="none" stroke="#222" stroke-width="1.8"/></svg>10.49 am</div><p>Lorem Ipsum is simply dummy text of the printing and typesetting industry</p></div>
      <div class="entry"><div class="time"><svg width="6" height="9" viewBox="0 0 6 9"><path d="M1 1l3.5 3.5L1 8" fill="none" stroke="#222" stroke-width="1.8"/></svg>9.49 am</div><p>Lorem Ipsum is simply dummy text of the printing and typesetting industry</p></div>
    </div>

    <div class="day" style="top:291px">
      <div class="day-title"><span class="ring"></span>Yesterday</div>
      <div class="entry"><div class="time"><svg width="6" height="9" viewBox="0 0 6 9"><path d="M1 1l3.5 3.5L1 8" fill="none" stroke="#222" stroke-width="1.8"/></svg>5.49 pm</div><p>Lorem Ipsum is simply dummy text of the printing and typesetting industry</p></div>
      <div class="entry"><div class="time"><svg width="6" height="9" viewBox="0 0 6 9"><path d="M1 1l3.5 3.5L1 8" fill="none" stroke="#222" stroke-width="1.8"/></svg>12.00 pm</div><p>Lorem Ipsum is simply dummy text of the printing and typesetting industry</p></div>
      <div class="entry"><div class="time"><svg width="6" height="9" viewBox="0 0 6 9"><path d="M1 1l3.5 3.5L1 8" fill="none" stroke="#222" stroke-width="1.8"/></svg>9.49 am</div><p>Lorem Ipsum is simply dummy text of the printing and typesetting industry</p></div>
    </div>
  </section>
</main>

<footer class="footer">Copyright © 2018. All Rights Reserved - Privacy Policy</footer>

</body>
</html>
```